Australian gym wear company needs facebook design

We need a facebook design for our clothing company 'Ironvale Sportswear". We produce gym wear for strength athletes such as powerlifters, weightlifters and strongman competitors.

Our t-shirt designs generally has a medieval theme (think knights and chivalry), I have attached a couple for you to look at, I would like to keep the current branding.. We already have a facebook page so feel free to have a look.

Target Market(s)

Strength athletes

Industry/Entity Type

Clothing

```html
<!DOCTYPE html>
<html lang="en">
<head>
<meta charset="utf-8">
<title>Ironvale Sportswear – Facebook Cover</title>
<link href="https://fonts.googleapis.com/css2?family=Graduate&display=swap" rel="stylesheet">
<style>
  :root {
    --steel-light: #f2f2f2;
    --steel-mid: #b9b9b9;
    --steel-dark: #3a3a3a;
    --crimson: #7c0d16;
    --crimson-deep: #3d0308;
    --ink: #120204;
  }
  html, body {
    margin: 0;
    padding: 0;
    width: 1200px;
    height: 444px;
    overflow: hidden;
    background: #ffffff;
  }
  .cover {
    position: relative;
    width: 1200px;
    height: 444px;
    overflow: hidden;
    background:
      repeating-linear-gradient(-30deg, rgba(255,255,255,0.35) 0 1px, rgba(0,0,0,0.12) 1px 2px, rgba(255,255,255,0) 2px 4px),
      repeating-linear-gradient(-28deg, rgba(0,0,0,0.18) 0 2px, rgba(255,255,255,0) 2px 9px),
      linear-gradient(150deg, var(--steel-mid) 0%, var(--steel-light) 22%, var(--steel-dark) 45%, var(--steel-light) 62%, var(--steel-mid) 78%, var(--steel-dark) 100%);
  }
  .brand-disc {
    position: absolute;
    left: -190px;
    top: -148px;
    width: 720px;
    height: 720px;
    border-radius: 50%;
    background: radial-gradient(circle at 55% 45%, var(--crimson) 0%, var(--crimson-deep) 100%);
    display: flex;
    align-items: center;
    justify-content: center;
  }
  .brand-disc__name {
    margin-left: 190px;
    font-family: "Graduate", serif;
    font-size: 44px;
    letter-spacing: 2px;
    color: var(--steel-light);
  }
  .headline {
    position: absolute;
    left: 556px;
    top: 120px;
    width: 630px;
    height: 210px;
    overflow: visible;
  }
  .headline__text {
    font-family: "Graduate", serif;
    fill: var(--crimson);
    stroke: var(--ink);
    stroke-width: 3px;
    paint-order: stroke fill;
  }
</style>
</head>
<body>
  <main class="cover">
    <div class="brand-disc">
      <span class="brand-disc__name">IRONVALE</span>
    </div>
    <svg class="headline" viewBox="0 0 630 210" aria-label="Ironvale Sportswear">
      <text class="headline__text" x="8" y="104" font-size="112" textLength="606" lengthAdjust="spacingAndGlyphs">IRONVALE</text>
      <text class="headline__text" x="8" y="192" font-size="86" textLength="458" lengthAdjust="spacingAndGlyphs">SPORTSWEAR</text>
    </svg>
  </main>
</body>
</html>
```